Phuket Thailand - Rental Villa Website

I have a villa for rent in Thailand and require a website - i need to demo pictures/walk through video, local attractions, villa facilities description plus seaonal rates and online booking.

Industry/Entity Type

Rental

Coding

Coded - Design and coding required

```html
<!DOCTYPE html>
<html lang="en">
<head>
<meta charset="utf-8">
<title>Andaman Cove Rental Villa</title>
<link rel="stylesheet" href="https://fonts.googleapis.com/css2?family=Cinzel:wght@400;700&family=PT+Sans:wght@400&display=swap">
<style>
  :root {
    --sand: #e0c9a0;
    --sand-light: #e8d3ae;
    --cocoa: #231810;
    --cocoa-mid: #3a2a1c;
    --taupe: #7a6a58;
    --taupe-light: #8d7d6a;
    --teal: #0f6f95;
    --white: #ffffff;
    --cream: #f2e6cc;
    --grey-bg: #e9e9e9;
    --black: #050403;
  }
  * { box-sizing: border-box; margin: 0; padding: 0; }
  html, body { width: 1003px; height: 1200px; overflow: hidden; background: var(--sand); }
  body { font-family: "PT Sans", Arial, sans-serif; color: var(--white); }
  .page { position: relative; width: 1003px; height: 1200px; }
  .abs { position: absolute; }

  /* header */
  .site-header { position: absolute; left: 29px; top: 29px; width: 943px; height: 97px; background: var(--cocoa); }
  .brand { position: absolute; left: 34px; top: 18px; font-family: "Cinzel", serif; font-weight: 400; color: var(--white); }
  .brand-name { font-size: 27px; line-height: 30px; letter-spacing: 0.5px; display: block; }
  .brand-sub { font-size: 11px; letter-spacing: 5px; display: block; padding-left: 40px; }
  .btn { display: block; position: absolute; background: var(--teal); color: var(--white); border-radius: 12px;
         font-size: 11.5px; text-align: center; line-height: 24px; height: 24px; text-decoration: none; letter-spacing: -0.2px; }
  .btn-book { left: 788px; top: 39px; width: 80px; }

  /* nav */
  .main-nav { position: absolute; left: 29px; top: 126px; width: 943px; height: 44px; background: var(--taupe); border-top: 2px solid #a39584; border-bottom: 6px solid var(--cocoa-mid); }
  .nav-pill { position: absolute; top: 9px; height: 24px; line-height: 24px; border-radius: 12px; background: var(--cocoa);
              color: var(--white); font-size: 11px; text-align: center; text-decoration: none; }
  .nav-pill.is-active { background: var(--sand-light); color: var(--cocoa); }

  /* hero */
  .hero { position: absolute; left: 29px; top: 176px; width: 943px; height: 424px; background: var(--cocoa); overflow: hidden; }
  .hero-photo { position: absolute; left: 0; top: 0; width: 943px; height: 323px;
    background: linear-gradient(180deg, #4f8fd0 0%, #a9cbe8 40%, #e6eef2 62%, #5fc7c4 75%, #3aa9a6 100%); }
  .hero-title { position: absolute; left: 44px; top: 42px; font-family: "Cinzel", serif; font-size: 38px; color: var(--cocoa); }
  .hero-rule { position: absolute; left: 44px; top: 85px; width: 406px; height: 2px; background: var(--teal); }
  .hero-text { position: absolute; left: 49px; top: 98px; width: 460px; font-size: 15.5px; line-height: 20px; color: #1b1b1b; }
  .feature-card { position: absolute; left: 575px; top: 27px; width: 357px; height: 269px; border: 5px solid var(--sand-light); background: rgba(45,32,20,0.82); }
  .feature-card h2 { position: absolute; left: 0; top: 14px; width: 100%; text-align: center; font-family: "Cinzel", serif; font-weight: 400; font-size: 32px; }
  .card-rule { position: absolute; height: 1px; background: #d8d0c4; }
  .feature-photo { position: absolute; left: 18px; top: 77px; width: 150px; height: 112px; background: linear-gradient(135deg, #7a6a58, #c9c0b2); }
  .feature-text { position: absolute; left: 187px; top: 75px; width: 160px; font-size: 12.5px; line-height: 16px; }
  .caption-band { position: absolute; left: 0; top: 323px; width: 943px; height: 50px; background: rgba(35,40,42,0.82);
                  font-family: "Cinzel", serif; font-size: 18px; line-height: 50px; text-align: center; color: var(--white); }
  .hero-foot-rule { position: absolute; left: 61px; top: 373px; width: 825px; height: 1px; background: #9a8f85; }

  /* features */
  .features { position: absolute; left: 29px; top: 611px; width: 943px; height: 331px;
              background: radial-gradient(ellipse at center, #ffffff 40%, var(--grey-bg) 100%); }
  .info-card { position: absolute; top: 26px; width: 301px; height: 277px; background: var(--cocoa); border: 5px solid var(--sand-light); }
  .info-card h3 { position: absolute; left: 3px; top: 3px; width: 285px; height: 40px; background: linear-gradient(90deg, #5a4b3c, var(--taupe-light));
                  font-family: "Cinzel", serif; font-weight: 400; font-size: 28px; line-height: 42px; text-align: center; }
  .info-photo { position: absolute; left: 3px; top: 77px; width: 130px; height: 122px; }
  .info-text { position: absolute; left: 152px; top: 73px; width: 140px; font-size: 12.5px; line-height: 16px; }
  .info-card .btn { left: 87px; top: 230px; width: 118px; }

  /* footer */
  .site-footer { position: absolute; left: 29px; top: 953px; width: 943px; height: 160px; background: var(--cocoa); }
  .footer-col { position: absolute; top: 23px; width: 182px; }
  .footer-col h4 { font-family: "Cinzel", serif; font-weight: 400; font-size: 16px; padding-left: 15px; height: 25px; }
  .footer-col .underline { height: 2px; background: linear-gradient(90deg, #4a3a2a, #b8a890, #4a3a2a); }
  .footer-col ul { list-style: none; padding: 14px 0 0 15px; }
  .footer-col li { font-size: 14px; line-height: 25.5px; }
  .footer-bar { position: absolute; left: 29px; top: 1113px; width: 943px; height: 54px; background: var(--black); }
  .footer-brand { position: absolute; left: 21px; top: 11px; font-family: "Cinzel", serif; color: var(--white); }
  .footer-brand .brand-name { font-size: 17px; line-height: 20px; }
  .footer-brand .brand-sub { font-size: 7px; letter-spacing: 3px; padding-left: 26px; }
  .footer-nav { position: absolute; top: 0; line-height: 54px; font-size: 11px; color: #d9d9d9; }
  .social-dot { position: absolute; top: 14px; width: 26px; height: 26px; border-radius: 50%; background: var(--sand-light); }
</style>
</head>
<body>
<div class="page">

  <header class="site-header">
    <div class="brand"><span class="brand-name">Andaman Cove</span><span class="brand-sub">RENTAL VILLA</span></div>
    <a class="btn btn-book" href="#">BOOK NOW</a>
  </header>

  <nav class="main-nav">
    <a class="nav-pill" style="left:67px;width:77px" href="#">HOME</a>
    <a class="nav-pill is-active" style="left:180px;width:106px" href="#">ABOUT THE VILLA</a>
    <a class="nav-pill" style="left:320px;width:92px" href="#">VIRTUAL TOUR</a>
    <a class="nav-pill" style="left:445px;width:81px" href="#">PRICING</a>
    <a class="nav-pill" style="left:559px;width:89px" href="#">AVAILABILITY</a>
    <a class="nav-pill" style="left:673px;width:80px" href="#">REVIEWS</a>
    <a class="nav-pill" style="left:788px;width:80px" href="#">CONTACT</a>
  </nav>

  <section class="hero">
    <div class="hero-photo" role="img" aria-label="Tropical beach with longtail boats on turquoise water and limestone islands under a blue sky"></div>
    <h1 class="hero-title">Things To Do</h1>
    <div class="hero-rule"></div>
    <p class="hero-text">Lorem ipsum dolor sit amet consectetur adipiscing elit, lorem ipsum sit amet elit consectetur elit.</p>

    <div class="feature-card">
      <h2>Vacation Villa</h2>
      <div class="card-rule" style="left:18px;top:63px;width:333px"></div>
      <div class="feature-photo" role="img" aria-label="Villa bedroom interior"></div>
      <p class="feature-text">lorem ipsum dolor sit amet consectetur und adipiscing elit sit amet lorem ipsum dolor sit amet consectetur und adipiscing elit sit amet ipsum lorem adipiscing sit consectetur elit.</p>
      <div class="card-rule" style="left:18px;top:207px;width:333px"></div>
      <a class="btn" style="left:121px;top:224px;width:119px" href="#">VIEW DETAILS</a>
    </div>

    <div class="caption-band">Wonderful Vacation Villa In The Most Sought-after Location By Tourists</div>
    <div class="hero-foot-rule"></div>
  </section>

  <section class="features">
    <article class="info-card" style="left:15px">
      <h3>Location</h3>
      <div class="card-rule" style="left:5px;top:59px;width:286px"></div>
      <div class="info-photo" role="img" aria-label="Villa exterior with tiled roof and garden" style="background:linear-gradient(135deg,#5d5850,#8a6e5c)"></div>
      <p class="info-text">lorem ipsum dolor sit amet consectetur und adipiscing elit sit amet lorem ipsum dolor sit amet consectetur und elit sit amet ipsum sit elit. ipsum lorem</p>
      <div class="card-rule" style="left:5px;top:211px;width:286px"></div>
      <a class="btn" href="#">VIEW DETAILS</a>
    </article>
    <article class="info-card" style="left:322px">
      <h3>Amenities</h3>
      <div class="card-rule" style="left:5px;top:59px;width:286px"></div>
      <div class="info-photo" role="img" aria-label="Infinity swimming pool" style="background:linear-gradient(180deg,#6d7f74,#1f8c86)"></div>
      <p class="info-text">lorem ipsum dolor sit amet consectetur und adipiscing elit sit amet lorem ipsum dolor sit amet consectetur und adipiscing elit sit amet sit consectetur elit.</p>
      <div class="card-rule" style="left:5px;top:211px;width:286px"></div>
      <a class="btn" href="#">VIEW DETAILS</a>
    </article>
    <article class="info-card" style="left:628px">
      <h3>Entertainment</h3>
      <div class="card-rule" style="left:5px;top:59px;width:286px"></div>
      <div class="info-photo" role="img" aria-label="Street of nightclubs with neon signs at night" style="background:linear-gradient(135deg,#1a1430,#b2262a 60%,#d9a23a)"></div>
      <p class="info-text">lorem ipsum dolor sit amet consectetur und adipiscing elit sit amet lorem ipsum dolor und adipiscing elit sit amet lorem adipiscing sit consectetur.</p>
      <div class="card-rule" style="left:5px;top:211px;width:286px"></div>
      <a class="btn" href="#">VIEW DETAILS</a>
    </article>
  </section>

  <footer class="site-footer">
    <div class="footer-col" style="left:48px">
      <h4>About the City</h4><div class="underline"></div>
      <ul><li>General Information</li><li>Important Numbers</li></ul>
    </div>
    <div class="footer-col" style="left:274px">
      <h4>Things to Do</h4><div class="underline"></div>
      <ul><li>Where to go</li><li>Nightlife &amp; Entertainment</li></ul>
    </div>
    <div class="footer-col" style="left:501px">
      <h4>Restaurants &amp; Bars</h4><div class="underline"></div>
      <ul><li>Restaurants</li><li>Bars &amp; Nightclubs</li></ul>
    </div>
    <div class="footer-col" style="left:737px">
      <h4>Contact Us</h4><div class="underline"></div>
      <ul><li>Social Page</li><li>Updates Feed</li><li>Email us</li></ul>
    </div>
  </footer>

  <div class="footer-bar">
    <div class="footer-brand"><span class="brand-name" style="display:block">Andaman Cove</span><span class="brand-sub" style="display:block">RENTAL VILLA</span></div>
    <span class="footer-nav" style="left:207px">HOME</span>
    <span class="footer-nav" style="left:264px">ABOUT THE VILLA</span>
    <span class="footer-nav" style="left:375px">VIRTUAL TOUR</span>
    <span class="footer-nav" style="left:471px">PRICING</span>
    <span class="footer-nav" style="left:536px">AVAILABILITY</span>
    <span class="footer-nav" style="left:626px">REVIEWS</span>
    <span class="footer-nav" style="left:696px">CONTACT</span>
    <span class="social-dot" style="left:791px" aria-label="Social page"></span>
    <span class="social-dot" style="left:839px" aria-label="Updates feed"></span>
    <span class="social-dot" style="left:888px" aria-label="Photo board"></span>
  </div>

</div>
</body>
</html>
```